Willowmere Equine Sanctuary Flyer Urgent

Willowmere Equine Sanctuary

Rescue • Rehabilitation • Sanctuary

Willowmere Equine Sanctuary provides a safe and ethical refuge for horses, ponies and donkeys who have nowhere else to go. Some arrive needing rehabilitation and careful retraining, while others find permanent sanctuary here due to age, injury or behavioural needs.

Our mission is simple: to improve the physical and psychological wellbeing of every animal in our care.

At Willowmere we focus on:
• Rescue and rehabilitation of horses in need
• Lifetime sanctuary for those who cannot be rehomed
• Education and advocacy for responsible horse care
• Equine rehabilitation services to help horses recover and thrive

Sponsor a Horse

One of the most meaningful ways to support our work is by sponsoring one of our residents. Each horse, pony or donkey only has one sponsor!

Your sponsorship helps provide:
• Hay and feed
• Veterinary care
• Hoof trimming and routine health care
• Rugs, shelter and daily care

Many of our horses will live out their lives here, and sponsorship ensures they are safe, well fed and cared for every single day.

Sponsorship starts from $15 - $25 per week / $60 -$100 per month.

How You Can Help

• Sponsor a horse
• Make a donation
• Share our work with others

Your support helps us continue to say yes to horses who need a second chance.

📍 Willowmere Park, Victoria
📧 clara@willowmerepark-example.org

📞 0400 519 627

Font styles to use
Serif
Sans Serif

Colors
F0912C
F2A743
F7CA91
FBE8D2
FDF5EE
EE7325
F08F49
F5BC92
FAE3D3
FDF4ED

Requirements
Should not have
• Photos not provided by Willowmere

```html
<!DOCTYPE html>
<html lang="en">
<head>
<meta charset="utf-8">
<title>Willowmere Equine Sanctuary – Flyer</title>
<link rel="stylesheet" href="https://fonts.googleapis.com/css2?family=Noto+Serif:wght@700&family=Roboto:wght@400;500;700&display=swap">
<style>
  :root {
    --orange-deep: #EE7325;
    --orange: #F08F49;
    --amber: #F0912C;
    --gold: #F2A743;
    --peach: #F7CA91;
    --peach-soft: #F5BC92;
    --cream: #FBE8D2;
    --blush: #FAE3D3;
    --paper: #FDF5EE;
    --paper-light: #FDF4ED;
    --brand-brown: #B4561D;
    --ink: #1E1A17;
  }
  * { box-sizing: border-box; margin: 0; padding: 0; }
  html, body { width: 785px; height: 1200px; overflow: hidden; background: var(--paper); }
  body { font-family: "Roboto", Arial, sans-serif; color: var(--ink); }

  .flyer {
    position: relative; width: 785px; height: 1200px; overflow: hidden;
    background: linear-gradient(180deg, var(--paper) 0%, var(--paper-light) 55%, var(--cream) 100%);
  }

  /* Header */
  .brand-mark {
    position: absolute; left: 84px; top: 60px; width: 118px; height: 118px;
    border-radius: 50%; background: var(--gold);
  }
  .brand-name {
    position: absolute; left: 240px; top: 50px;
    font-family: "Noto Serif", Georgia, serif; font-weight: 700;
    font-size: 45px; line-height: 52px; color: var(--brand-brown); letter-spacing: -0.3px;
  }
  .tagline {
    position: absolute; left: 241px; top: 158px;
    font-size: 20px; font-weight: 500; color: var(--brand-brown);
  }

  /* Intro */
  .photo {
    position: absolute; border-radius: 8px;
  }
  .photo--herd {
    left: 59px; top: 198px; width: 250px; height: 178px;
    background: linear-gradient(160deg, #9aa67a 0%, #7a5236 45%, #d8cfc2 100%);
  }
  .intro {
    position: absolute; left: 322px; top: 198px; width: 440px;
    font-size: 15.5px; line-height: 18.5px;
  }
  .intro p + p { margin-top: 9px; }

  /* Focus block */
  .section-band {
    position: absolute; height: 40px; border-radius: 8px;
    background: linear-gradient(90deg, var(--orange-deep), var(--orange));
    font-family: "Noto Serif", Georgia, serif; font-weight: 700;
    color: var(--paper); font-size: 24px; line-height: 40px; padding-left: 20px;
  }
  .focus-band { left: 55px; top: 392px; width: 665px; }
  .focus-panel {
    position: absolute; left: 55px; top: 426px; width: 665px; height: 118px;
    border-radius: 0 0 10px 10px; background: var(--blush); opacity: 0.9;
  }
  .shoe-list { position: absolute; list-style: none; font-size: 16px; }
  .shoe-list li { display: flex; align-items: center; height: 24px; }
  .shoe-list svg { width: 16px; height: 16px; margin-right: 10px; flex: none; }
  .focus-list { left: 73px; top: 441px; }

  /* Sponsor */
  .sponsor-panel {
    position: absolute; left: 55px; top: 556px; width: 665px; height: 300px;
    border-radius: 10px; background: var(--blush);
  }
  .sponsor-title {
    position: absolute; left: 74px; top: 562px;
    font-family: "Noto Serif", Georgia, serif; font-weight: 700;
    font-size: 35px; color: var(--brand-brown);
  }
  .sponsor-lead {
    position: absolute; left: 74px; top: 610px; width: 400px;
    font-size: 15px; line-height: 18px;
  }
  .sponsor-lead .note { font-size: 14.5px; letter-spacing: -0.2px; }
  .provides {
    position: absolute; left: 74px; top: 672px; font-size: 15.5px; line-height: 18px;
  }
  .provides ul { list-style: none; }
  .provides li::before { content: "•"; margin: 0 9px 0 4px; }
  .photo--pair {
    left: 465px; top: 567px; width: 240px; height: 196px;
    background: linear-gradient(150deg, #c9d4e3 0%, #8a5232 50%, #4a2a1a 100%);
  }
  .sponsor-close {
    position: absolute; left: 74px; top: 775px; width: 630px;
    font-size: 15.5px; line-height: 18px;
  }
  .price {
    position: absolute; left: 74px; top: 822px;
    font-size: 16px; font-weight: 700; color: var(--brand-brown); letter-spacing: -0.1px;
  }

  /* Help */
  .help-band { left: 55px; top: 872px; width: 310px; font-size: 24px; }
  .help-list { left: 73px; top: 922px; font-weight: 700; }
  .help-list li { height: 23px; }
  .closing {
    position: absolute; left: 0; top: 1002px; width: 785px; text-align: center;
    font-size: 17px; line-height: 19px;
  }

  /* Footer */
  .landscape { position: absolute; left: 0; top: 1022px; width: 785px; height: 178px; }
  .contact {
    position: absolute; left: 0; top: 1090px; width: 785px;
    display: flex; flex-direction: column; align-items: center;
    font-size: 20px; font-weight: 700; line-height: 27px;
  }
  .contact li { list-style: none; display: flex; align-items: center; }
  .contact svg { width: 18px; height: 18px; margin-right: 8px; fill: var(--ink); }
</style>
</head>
<body>
<main class="flyer">

  <header>
    <div class="brand-mark" aria-hidden="true"></div>
    <h1 class="brand-name">Willowmere<br>Equine Sanctuary</h1>
    <p class="tagline">Rescue • Rehabilitation • Sanctuary</p>
  </header>

  <div class="photo photo--herd" role="img" aria-label="Photo of a herd of bay, grey and white horses and ponies standing together in a paddock"></div>
  <div class="intro">
    <p>Willowmere Equine Sanctuary provides a safe and ethical refuge for horses, ponies and donkeys who have nowhere else to go. Some arrive needing rehabilitation and careful retraining, while others find permanent sanctuary here due to age, injury or behavioural needs.</p>
    <p>Our mission is simple: to improve the physical and psychological wellbeing of every animal in our care.</p>
  </div>

  <section>
    <div class="focus-panel"></div>
    <h2 class="section-band focus-band">At Willowmere we focus on:</h2>
    <ul class="shoe-list focus-list">
      <li><svg viewBox="0 0 16 16"><path d="M3 2v6a5 5 0 0 0 10 0V2" fill="none" stroke="#F0912C" stroke-width="2.6" stroke-linecap="round"/></svg><span><b>Rescue</b> and <b>rehabilitation</b> of horses in need</span></li>
      <li><svg viewBox="0 0 16 16"><path d="M3 2v6a5 5 0 0 0 10 0V2" fill="none" stroke="#F0912C" stroke-width="2.6" stroke-linecap="round"/></svg><span><b>Lifetime sanctuary</b> for those who cannot be rehomed</span></li>
      <li><svg viewBox="0 0 16 16"><path d="M3 2v6a5 5 0 0 0 10 0V2" fill="none" stroke="#F0912C" stroke-width="2.6" stroke-linecap="round"/></svg><span><b>Education</b> and <b>advocacy</b> for responsible horse care</span></li>
      <li><svg viewBox="0 0 16 16"><path d="M3 2v6a5 5 0 0 0 10 0V2" fill="none" stroke="#F0912C" stroke-width="2.6" stroke-linecap="round"/></svg><span><b>Equine rehabilitation services</b> to help horses recover and thrive</span></li>
    </ul>
  </section>

  <section>
    <div class="sponsor-panel"></div>
    <h2 class="sponsor-title">Sponsor a Horse</h2>
    <p class="sponsor-lead">One of the most meaningful ways to support our work is by sponsoring one of our residents. <span class="note">Each horse, pony or donkey only has one sponsor!</span></p>
    <div class="provides">
      <p>Your sponsorship helps provide:</p>
      <ul>
        <li>Hay and feed</li>
        <li>Veterinary care</li>
        <li>Hoof trimming and routine health care</li>
        <li>Rugs, shelter and daily care.</li>
      </ul>
    </div>
    <div class="photo photo--pair" role="img" aria-label="Photo of two bay horses standing close together, heads touching"></div>
    <p class="sponsor-close">Many of our horses will live out their lives here, and sponsorship ensures they are safe, well fed and cared for every single day.</p>
    <p class="price">Sponsorship starts from $15 - $25 per week / $60 -$100 per month.</p>
  </section>

  <section>
    <h2 class="section-band help-band">How You Can Help</h2>
    <ul class="shoe-list help-list">
      <li><svg viewBox="0 0 16 16"><path d="M3 2v6a5 5 0 0 0 10 0V2" fill="none" stroke="#F0912C" stroke-width="2.6" stroke-linecap="round"/></svg>Sponsor a horse</li>
      <li><svg viewBox="0 0 16 16"><path d="M3 2v6a5 5 0 0 0 10 0V2" fill="none" stroke="#F0912C" stroke-width="2.6" stroke-linecap="round"/></svg>Make a donation</li>
      <li><svg viewBox="0 0 16 16"><path d="M3 2v6a5 5 0 0 0 10 0V2" fill="none" stroke="#F0912C" stroke-width="2.6" stroke-linecap="round"/></svg>Share our work with others</li>
    </ul>
    <p class="closing">Your support helps us continue to say yes to<br>horses who need a second chance.</p>
  </section>

  <footer>
    <svg class="landscape" viewBox="0 0 785 178" preserveAspectRatio="none" role="img" aria-label="Illustrated rolling hills landscape with horse silhouettes and a tree">
      <defs>
        <linearGradient id="hills" x1="0" y1="0" x2="0" y2="1">
          <stop offset="0" stop-color="#F7CA91"/>
          <stop offset="0.55" stop-color="#F2A743"/>
          <stop offset="1" stop-color="#F0912C"/>
        </linearGradient>
      </defs>
      <path d="M0 40 C150 10 300 30 420 22 C560 12 680 30 785 18 L785 178 L0 178 Z" fill="url(#hills)"/>
    </svg>
    <ul class="contact">
      <li><svg viewBox="0 0 24 24"><path d="M12 2a7 7 0 0 0-7 7c0 5 7 13 7 13s7-8 7-13a7 7 0 0 0-7-7zm0 9.5A2.5 2.5 0 1 1 12 6.5a2.5 2.5 0 0 1 0 5z"/></svg>Willowmere Park, Victoria</li>
      <li><svg viewBox="0 0 24 24"><path d="M2 5h20v14H2zm2 2v.5l8 5 8-5V7zm0 3v7h16v-7l-8 5z"/></svg>clara@willowmerepark-example.org</li>
      <li><svg viewBox="0 0 24 24"><path d="M6.6 10.8a15 15 0 0 0 6.6 6.6l2.2-2.2a1 1 0 0 1 1-.25 11.4 11.4 0 0 0 3.6.6 1 1 0 0 1 1 1V20a1 1 0 0 1-1 1A17 17 0 0 1 3 4a1 1 0 0 1 1-1h3.5a1 1 0 0 1 1 1c0 1.25.2 2.45.6 3.6a1 1 0 0 1-.25 1z"/></svg>0400 519 627</li>
    </ul>
  </footer>

</main>
</body>
</html>
```